Prestige Car Bodyshop Business Card

We are a car bodyshop based in the UK. Our customer base is mainly prestige high-value vehicles. I am looking for a classy and stylish business card design for my staff to give out to customers, with their direct email and phone number, as well as our main email and phone number with address details

I am also looking to have a general business card design with just our main company address and contact details, but also have a space to add a manufacturer approval logo (i.e Velmora, Orek, Tovalo etc... logo) in the corner somewhere.

I do not particularly want any outlines or pictures of cars on the card, I would just like a quality high-end look.

Please feel free to get in touch if you have any questions or queries?

Many Thanks

Malcolm

Target Market(s)

Prestige vehicle owners

Industry/Entity Type

Automotive

Contact Information for Business Card

I am looking for a classy and stylish business card design for my staff to give out to customers, with their direct email and phone number, as well as our main email and phone number with address details

Font styles to use
Sans Serif

Colors

Designer to choose colors to be used in the design.

Requirements
Nice to have
• I do not particularly want any outlines or pictures of cars on the card, I would just like a quality high-end look.

```html
<!DOCTYPE html>
<html lang="en">
<head>
<meta charset="utf-8">
<title>RJ Harlow Business Card</title>
<link rel="stylesheet" href="https://fonts.googleapis.com/css2?family=Lato:wght@300;400;700&display=swap">
<style>
  :root {
    --page: #ffffff;
    --navy-top: #252650;
    --navy-bottom: #2b4797;
    --white: #ffffff;
    --ink: #1f1f22;
    --badge: #8a8a8f;
  }
  * { margin: 0; padding: 0; box-sizing: border-box; }
  html, body {
    width: 1200px; height: 758px; overflow: hidden;
    background: var(--page);
    font-family: "Lato", Arial, sans-serif;
  }
  .canvas { position: relative; width: 1200px; height: 758px; }
  .card {
    position: absolute;
    box-shadow: 6px 10px 22px rgba(0, 0, 0, 0.18);
  }
  .card--front {
    left: 103px; top: 117px; width: 470px; height: 470px;
    background: linear-gradient(180deg, var(--navy-top) 0%, var(--navy-top) 22%, var(--navy-bottom) 85%, var(--navy-bottom) 100%);
  }
  .brand-name {
    position: absolute; left: 0; width: 100%; top: 196px;
    text-align: center; color: var(--white);
    font-weight: 300; font-size: 50px; letter-spacing: 1px; line-height: 1;
    white-space: nowrap;
  }
  .brand-rule {
    position: absolute; left: 105px; width: 260px; top: 262px;
    height: 2px; background: var(--white);
  }
  .brand-tagline {
    position: absolute; left: 0; width: 100%; top: 270px;
    text-align: center; color: var(--white);
    font-weight: 400; font-size: 16.5px; letter-spacing: 0.2px;
  }
  .card--back {
    left: 631px; top: 118px; width: 465px; height: 466px;
    background: var(--white);
    color: var(--ink);
  }
  .address {
    position: absolute; left: 0; width: 100%; top: 88px;
    text-align: center; font-weight: 300; font-size: 30px; line-height: 29.5px;
    font-style: normal;
  }
  .contacts {
    position: absolute; left: 0; width: 100%; top: 306px;
    text-align: center; font-weight: 300; font-size: 21px; line-height: 30px;
    white-space: nowrap;
  }
  .contacts b { font-weight: 700; }
  .contacts .web { font-weight: 400; }
  .approvals {
    position: absolute; left: 33px; top: 392px;
  }
</style>
</head>
<body>
<main class="canvas">
  <section class="card card--front" aria-label="Card front">
    <div class="brand-name">RJ HARLOW</div>
    <div class="brand-rule"></div>
    <div class="brand-tagline">ACCIDENT REPAIR CENTRE</div>
  </section>

  <section class="card card--back" aria-label="Card back">
    <address class="address">
      Kestrel Road,<br>
      Brookfield Common<br>
      Ashworth,<br>
      Bristol BS30 9XT<br>
      United Kingdom
    </address>
    <div class="contacts">
      <div><b>T:</b> 0117 496 0173&nbsp; <b>F:</b> 0117 496 0621</div>
      <div><b>E:</b> info@rjharlow.co.uk <span class="web">www.rjharlow.co.uk</span></div>
    </div>
    <svg class="approvals" width="398" height="28" viewBox="0 0 398 28" role="img" aria-label="Manufacturer approval badges">
      <g fill="var(--badge)">
        <rect x="0" y="8" width="44" height="12" rx="2"/>
        <ellipse cx="80" cy="14" rx="22" ry="10"/>
        <rect x="118" y="11" width="46" height="6" rx="2"/>
        <circle cx="182" cy="14" r="11"/>
        <rect x="206" y="7" width="40" height="14" rx="7"/>
        <rect x="264" y="5" width="18" height="18" rx="2"/>
        <circle cx="305" cy="14" r="9"/>
        <ellipse cx="343" cy="14" rx="21" ry="10"/>
        <circle cx="386" cy="14" r="11"/>
      </g>
    </svg>
  </section>
</main>
</body>
</html>
```